Design Business Cards

I need a new business card designed in two versions, one an International version and one a Japanese version.

Please ensure to submit designer files so we can edit it ourselves after the contest. We require the following file formats at minimum (AI, PSD, PNG).

I have attached 4 examples of letterpress business cards and the kind of style we want. Below you will find all the data for the front and back of the two cards, please come up with your own layout for how you think it should be best presented based on the data below, brief and examples.

I have also attached our company logo file.

Design Brief:

Simple and elegant business card, white, two sided. We will be producing two versions an international version and a Japanese version. We will require finished designs for both. These will be printed via letterpress and this should be considered when creating the design.

The (text) indicates what the information is and should not appear on the design. This is just for your reference.

International Front:

Company Logo

International Back:

Company Logo

Desmond Hartwick (Name)
Commercial Manager (Title)
+61 455 287 913 (Telephone)
randall@[login to view URL] (Email)

2078/4 Larkspur Rd
Melbourne, Vic, 3004
Australia
(Address)

United Kingdom | Australia | Hong Kong
(Worldwide Office Locations)

Japanese Front:

Company Logo

Desmond Hartwick (Name)
コマーシャルマネージャー (Title)

2078/4 Larkspur Rd
Melbourne, Vic, 3004
Australia
(Address)

イギリス|オーストラリア|香港

Japanese Back:

Company Logo

Desmond Hartwick (Name)

2078/4 Larkspur Rd
Melbourne, Vic, 3004
Australia
(Address)

```html
<!DOCTYPE html>
<html lang="en">
<head>
<meta charset="utf-8">
<title>Halden Events – Business Card</title>
<link rel="stylesheet" href="https://fonts.googleapis.com/css2?family=Montserrat:wght@500;600;700&family=Open+Sans:wght@400;600&display=swap">
<style>
  :root {
    --backdrop: #aaaaaa;
    --card: #f7f7f7;
    --ink: #4a4a4a;
    --ink-soft: #6a6a6a;
    --rule: #5a5a5a;
    --facet-light: #f4f4f4;
    --facet-mid: #d8d8d8;
  }
  * { box-sizing: border-box; margin: 0; padding: 0; }
  html, body { width: 1016px; height: 1200px; overflow: hidden; }
  body {
    background: var(--backdrop);
    font-family: "Open Sans", sans-serif;
    color: var(--ink);
    position: relative;
  }
  .card {
    position: absolute;
    left: 158px;
    width: 700px;
    height: 400px;
    background: var(--card);
    box-shadow: 0 10px 30px rgba(0,0,0,0.18);
    overflow: hidden;
  }
  .card--front { top: 150px; }
  .card--back { top: 650px; }

  .facet-pattern {
    position: absolute;
    inset: 0;
    background: linear-gradient(135deg, var(--facet-light) 0%, var(--facet-mid) 40%, var(--facet-light) 65%, var(--facet-mid) 100%);
  }
  .front-wordmark {
    position: absolute;
    inset: 0;
    display: flex;
    flex-direction: column;
    align-items: center;
    justify-content: center;
    font-family: "Montserrat", sans-serif;
    font-weight: 700;
    color: var(--ink);
    text-align: center;
    line-height: 1;
  }
  .front-wordmark .name-main { font-size: 64px; letter-spacing: 2px; }
  .front-wordmark .name-sub { font-size: 26px; letter-spacing: 10px; margin-top: 12px; padding-left: 10px; }

  .back-wordmark {
    position: absolute;
    left: 56px;
    top: 92px;
    width: 200px;
    font-family: "Montserrat", sans-serif;
    font-weight: 700;
    color: var(--ink);
    line-height: 1;
    text-align: center;
  }
  .back-wordmark .name-main { font-size: 38px; letter-spacing: 1px; }
  .back-wordmark .name-sub { font-size: 18px; letter-spacing: 8px; margin-top: 10px; padding-left: 8px; }

  .divider {
    position: absolute;
    left: 275px;
    top: 72px;
    width: 2px;
    height: 120px;
    background: var(--rule);
  }
  .contact {
    position: absolute;
    left: 298px;
    top: 74px;
  }
  .contact .person-name {
    font-family: "Montserrat", sans-serif;
    font-weight: 600;
    font-size: 24px;
    line-height: 1.2;
    color: var(--ink);
  }
  .contact .person-title {
    font-size: 15px;
    color: var(--ink-soft);
    margin-top: 2px;
    margin-bottom: 12px;
  }
  .contact-line {
    display: flex;
    align-items: center;
    gap: 10px;
    font-size: 13px;
    font-weight: 600;
    color: var(--ink);
    height: 20px;
  }
  .contact-line svg { width: 13px; height: 13px; fill: var(--ink); flex: none; }

  .address {
    position: absolute;
    left: 72px;
    top: 262px;
    font-size: 12px;
    line-height: 1.4;
    color: var(--ink);
  }
  .address .label { font-weight: 600; font-size: 13px; margin-bottom: 2px; }

  .offices {
    position: absolute;
    right: 64px;
    bottom: 56px;
    font-size: 12px;
    color: var(--ink);
  }
</style>
</head>
<body>

  <section class="card card--front" aria-label="Card front">
    <div class="facet-pattern" role="img" aria-label="Light grey faceted geometric background pattern"></div>
    <div class="front-wordmark">
      <span class="name-main">HALDEN</span>
      <span class="name-sub">EVENTS</span>
    </div>
  </section>

  <section class="card card--back" aria-label="Card back">
    <div class="back-wordmark">
      <div class="name-main">HALDEN</div>
      <div class="name-sub">EVENTS</div>
    </div>

    <div class="divider"></div>

    <div class="contact">
      <div class="person-name">Desmond Hartwick</div>
      <div class="person-title">Commercial Manager</div>
      <div class="contact-line">
        <svg viewBox="0 0 16 16" aria-hidden="true"><path d="M3.5 1h2.5l1.2 3.4-1.6 1.2a8 8 0 0 0 4.8 4.8l1.2-1.6L15 10v2.5A2 2 0 0 1 13 14.5 12.5 12.5 0 0 1 1.5 3 2 2 0 0 1 3.5 1z"/></svg>
        <span>+61 455 287 913</span>
      </div>
      <div class="contact-line">
        <svg viewBox="0 0 16 16" aria-hidden="true"><path d="M1 3h14v10H1z M2 4.2v.6l6 4 6-4v-.6z" fill-rule="evenodd"/></svg>
        <span>desmond@haldenevents.com</span>
      </div>
      <div class="contact-line">
        <svg viewBox="0 0 16 16" aria-hidden="true"><circle cx="8" cy="8" r="7"/></svg>
        <span>www.haldenevents.com</span>
      </div>
    </div>

    <div class="address">
      <div class="label">Address :</div>
      <div>2078/4 Larkspur Rd</div>
      <div>Melbourne , Vic , 3004</div>
      <div>Australia</div>
    </div>

    <div class="offices">United Kingdom &nbsp;|&nbsp; Australia &nbsp;|&nbsp; Hong Kong</div>
  </section>

</body>
</html>
```